Health Benefits Association Website Design

The Unified Household Wellspring Alliance (UHWA) is an organization formed for the purpose of providing its members better value for selected health benefits and services. Members can use the association benefits either in conjunction with or independently of other medical insurance they may have. Some of the benefits available include discounted dental and vision care and prescription mail order services. There is no limitation on who can join. This membership will be primarily marketed as a way to enhance the value of a fixed benefit health insurance plan although members do not have to have the insurance plan join the association.

We are seeking a design for a website to be used for consumers to get information about membership and for current members to be able to access their benefits. The website should include:

1) A landing page to provide a description of the UHWA

2) A secondary page that can be duplicated that will:
a. Provide a list of benefits
b. Provide a membership enrollment form
c. Provide a member’s only access page
d. Provide a contact page for more information

We are seeking a modern but conservative design that will reflect value, simplicity and good health. The site design will also need to be compatible for use with mobile phones and tablets.

A copy of the association logo is included with the submission. It will also need to be incorporated into the website design. Layouts of similar association websites have also been included for reference.

Target Market(s)

Ages 25 to 65 unmarried, married with no children, professionals, self-employed, active and healthy

Industry/Entity Type

Health And Wellness

Number of Pages Required

2 page

Font styles to use
Sans Serif

Colors

Designer to choose colors to be used in the design.

Requirements
Must have
• UHWA Logo (attached). Use colors from the logo in the website design.
Nice to have
• Graphics, if used, should convey health and fitness and skew toward a diverse array of adults 25 to 40.

```html
<!DOCTYPE html>
<html lang="en">
<head>
<meta charset="utf-8">
<title>Unified Household Wellspring Alliance</title>
<link href="https://fonts.googleapis.com/css2?family=Arimo:wght@400;700&family=Tinos:wght@400;700&display=swap" rel="stylesheet">
<style>
:root{
  --page:#f4f4f4;
  --olive:#8d964f;
  --olive-dark:#6f7a38;
  --olive-line:#a4ac6e;
  --yellow:#fbcd1e;
  --text:#3a3a3a;
  --body:#444;
  --rule:#cfcfcf;
  --white:#fff;
}
*{margin:0;padding:0;box-sizing:border-box}
html,body{width:673px;height:1200px;overflow:hidden;background:var(--page)}
body{position:relative;font-family:"Arimo",Arial,sans-serif;color:var(--text)}
a{color:inherit;text-decoration:none}
.abs{position:absolute}

/* header */
.brand{left:76px;top:34px;width:88px;text-align:center;font-family:"Tinos","Times New Roman",serif;font-weight:700;color:var(--olive);font-size:12px;line-height:14px;letter-spacing:.3px}
.brand-mark{display:block;width:26px;height:26px;border-radius:50%;background:var(--yellow);margin:0 auto 6px}
.social-top{top:22px;left:511px;display:flex;gap:6px}
.social-top span{width:17px;height:17px;border-radius:50%;background:var(--olive);display:block;box-shadow:inset 0 0 0 2px #a7af6f}
.social-top span.active{background:var(--yellow);box-shadow:inset 0 0 0 2px #fde27a}
.search{left:484px;top:57px;width:110px;height:23px;border:1px solid var(--rule);background:var(--white);font-size:8px;color:#aaa;padding:7px 8px}
.search svg{position:absolute;right:6px;top:5px}
.nav{top:100px;font-size:11px;letter-spacing:.4px;color:var(--text)}
.nav-active{border-bottom:3px solid var(--olive);padding-bottom:3px}
.dropdown{left:353px;top:128px;width:86px;background:var(--olive);z-index:3}
.dropdown a{display:block;height:24px;line-height:24px;padding-left:7px;color:var(--white);font-family:"Tinos",serif;font-size:10px;border-bottom:1px solid var(--olive-line)}

/* hero */
.hero{left:72px;top:132px;width:530px;height:244px;
  background:
    radial-gradient(ellipse 120px 150px at 130px 130px,rgba(196,150,112,.55),transparent 70%),
    radial-gradient(ellipse 90px 120px at 270px 110px,rgba(150,96,70,.45),transparent 70%),
    radial-gradient(ellipse 180px 90px at 110px 230px,rgba(225,215,200,.8),transparent 70%),
    linear-gradient(90deg,#c7ad93 0%,#e3d7c8 35%,#efebe5 62%,#fafaf9 100%)}
.hero-bar{left:72px;top:376px;width:530px;height:4px;background:var(--yellow)}
.arrow{font-size:22px;color:#555;top:244px}
.slogan,.slogan-2{color:var(--white);font-family:"Tinos",serif;font-size:15px;line-height:22px;padding-left:8px;letter-spacing:.4px;height:22px}
.slogan{left:326px;top:228px;width:262px;background:var(--yellow)}
.slogan-2{left:326px;top:257px;width:243px;background:var(--olive)}
.hero-text{left:329px;top:286px;width:226px;font-size:8px;line-height:10px;color:#333}

/* sections */
.section-kicker{left:0;width:673px;text-align:center;font-family:"Tinos",serif;color:#555}
.rule{left:72px;width:530px;height:1px;background:var(--rule)}
.intro{left:80px;width:514px;text-align:center;font-size:8px;line-height:18px;color:var(--text);letter-spacing:.3px}
.card{width:166px}
.card-img{height:104px;border-bottom:3px solid var(--yellow)}
.card h3{font-family:"Tinos",serif;font-weight:400;font-size:9px;letter-spacing:.3px;margin-top:10px;color:#333}
.card p{font-size:7.5px;line-height:9px;color:var(--body);margin-top:3px}
.btn{display:inline-block;margin-top:12px;border:1px solid #888;font-size:7.5px;padding:5px 9px;color:var(--body);background:var(--white)}
.quote{width:248px;height:78px;background:var(--white);border:1px solid #ddd;border-bottom-width:3px}
.quote.yellow{border-bottom-color:var(--yellow)}
.quote.olive{border-bottom-color:var(--olive)}
.avatar{position:absolute;left:8px;top:8px;width:60px;height:60px;border-radius:50%;border:3px solid #ddd;background:radial-gradient(circle at 50% 40%,#c9a184,#7d6554 75%)}
.avatar.light{background:radial-gradient(circle at 50% 45%,#efcfae,#c08d5c 75%)}
.quote-mark{position:absolute;left:74px;top:6px;font-family:"Tinos",serif;font-size:30px;color:#ccc}
.quote p{position:absolute;left:78px;top:25px;width:162px;font-size:7.5px;line-height:9px;color:var(--body)}
.quote cite{position:absolute;right:10px;top:56px;font-style:normal;font-size:7.5px;color:var(--body)}

/* footer */
.footer{left:0;top:1006px;width:673px;height:172px;background:var(--olive);color:var(--white)}
.footer-brand{left:78px;top:42px;width:80px;text-align:center;font-family:"Tinos",serif;font-weight:700;font-size:12px;line-height:14px;color:var(--white)}
.footer-brand .brand-mark{background:var(--white)}
.footer-text{left:185px;top:40px;width:170px;font-size:8px;line-height:9.5px;color:var(--white)}
.footer h4{font-family:"Tinos",serif;font-weight:400;font-size:11px;letter-spacing:1px;padding-bottom:8px;border-bottom:1px solid var(--olive-line);width:108px;color:var(--white)}
.footer ul{list-style:none;margin-top:6px}
.footer li{font-family:"Tinos",serif;font-size:8px;height:19.5px;line-height:19.5px;display:flex;align-items:center;gap:6px;color:var(--white)}
.dot{width:5px;height:5px;border-radius:50%;background:var(--white)}
.ring{width:10px;height:10px;border-radius:50%;background:var(--white)}
.copyright{left:0;top:1178px;width:673px;height:22px;background:var(--olive-dark);color:var(--white);font-family:"Tinos",serif;font-size:8.5px;text-align:center;line-height:22px;letter-spacing:.3px}
</style>
</head>
<body>

<header>
  <div class="abs brand"><span class="brand-mark"></span>Unified Household Wellspring Alliance</div>
  <div class="abs social-top" aria-label="Social links">
    <span aria-label="Friendbook"></span><span class="active" aria-label="Searchplus"></span><span aria-label="Chirper"></span><span aria-label="Snapgram"></span>
  </div>
  <div class="abs search">Search keyword
    <svg width="11" height="11" viewBox="0 0 11 11"><circle cx="6.5" cy="4.5" r="3.5" fill="none" stroke="#999"/><line x1="4" y1="7" x2="1" y2="10" stroke="#999"/></svg>
  </div>
  <nav>
    <span class="abs nav" style="left:209px">Home</span>
    <span class="abs nav" style="left:274px">About us</span>
    <span class="abs nav nav-active" style="left:355px">Benefits</span>
    <span class="abs nav" style="left:437px">Our Services</span>
    <span class="abs nav" style="left:540px">Contact us</span>
  </nav>
  <div class="abs dropdown"><a href="#">Demo Link</a><a href="#">Demo Link</a><a href="#">Demo Link</a></div>
</header>

<section>
  <div class="abs hero" role="img" aria-label="Photo of a smiling doctor talking with a patient"></div>
  <span class="abs arrow" style="left:94px">&#10094;</span>
  <span class="abs arrow" style="left:570px">&#10095;</span>
  <div class="abs slogan">Slogan or Heading text goes here</div>
  <div class="abs slogan-2">Second sentence sample here.</div>
  <p class="abs hero-text">Lorem ipsum dolor sit amet, consectetur adipiscing elit. Curabitur lacinia pretium risus ac euismod. Aliquam auctor convallis mattis. Maecenas ornare augue vel nibh molestie, nec ultrices velit tincidunt.</p>
  <div class="abs hero-bar"></div>
</section>

<section>
  <div class="abs section-kicker" style="top:399px;font-size:11px;letter-spacing:.5px">Welcome to</div>
  <div class="abs section-kicker" style="top:414px;font-size:13px;color:var(--olive);letter-spacing:.8px">Unified Household Wellspring Alliance</div>
  <div class="abs rule" style="top:442px"></div>
  <p class="abs intro" style="top:460px">Lorem ipsum dolor sit amet, consectetur adipiscing elit. Curabitur lacinia pretium risus ac euismod. A ictor convallis mattis. Maecenas ornare augue vel nibh molestie, nec ultrices velit tincidunt. Aliquam convallis mattis.Aliquam auctor Maecenas ornare augue vel nibh molestie, nec ultrices velit tincidunt.</p>

  <article class="abs card" style="left:76px;top:535px">
    <div class="card-img" role="img" aria-label="Photo of a doctor reviewing notes with a senior patient" style="background:radial-gradient(ellipse 60px 80px at 60% 65%,rgba(120,112,100,.45),transparent 70%),linear-gradient(120deg,#f3f1ec,#d2cdc6 55%,#aaa49c)"></div>
    <h3>TITLE OF THIS LINK GOES HERE</h3>
    <p>Lorem ipsum dolor sit amet, consectetur adipiscing elit. Curabitur lacinia pretium risus ac euismod. A ictor convallis mattis.</p>
    <span class="btn">Read more</span>
  </article>
  <article class="abs card" style="left:253px;top:535px">
    <div class="card-img" role="img" aria-label="Photo of a doctor examining a patient's knee in a clinic" style="background:radial-gradient(ellipse 50px 70px at 65% 60%,rgba(60,70,95,.45),transparent 70%),linear-gradient(180deg,#f1f2f2,#c9ccd0 60%,#9ea3aa)"></div>
    <h3>TITLE OF THIS LINK GOES HERE</h3>
    <p>Lorem ipsum dolor sit amet, consectetur adipiscing elit. Curabitur lacinia pretium risus ac euismod. A ictor convallis mattis.</p>
    <span class="btn">Read more</span>
  </article>
  <article class="abs card" style="left:430px;top:535px">
    <div class="card-img" role="img" aria-label="Photo of a patient at a dental check-up" style="background:radial-gradient(ellipse 60px 50px at 35% 85%,rgba(90,180,210,.6),transparent 70%),radial-gradient(ellipse 70px 60px at 70% 40%,rgba(214,170,140,.6),transparent 70%),linear-gradient(135deg,#cdbcb0,#e3d3c8 50%,#d9a7a7)"></div>
    <h3>TITLE OF THIS LINK GOES HERE</h3>
    <p>Lorem ipsum dolor sit amet, consectetur adipiscing elit. Curabitur lacinia pretium risus ac euismod. A ictor convallis mattis.</p>
    <span class="btn">Read more</span>
  </article>
</section>

<section>
  <div class="abs section-kicker" style="top:759px;font-size:14px;letter-spacing:.6px">What <span style="color:var(--olive)">Our Member</span> says</div>
  <div class="abs rule" style="top:790px"></div>
  <p class="abs intro" style="top:813px">Lorem ipsum dolor sit amet, consectetur adipiscing elit. Curabitur lacinia pretium risus ac euismod. A ictor convallis mattis. Maecenas ornare augue vel nibh molestie, nec ultrices velit tincidunt. Aliquam convallis mattis.Aliquam auctor Maecenas ornare augue vel nibh molestie, nec ultrices velit tincidunt.</p>

  <blockquote class="abs quote yellow" style="left:80px;top:882px">
    <div class="avatar" role="img" aria-label="Portrait photo of member John Doe"></div>
    <span class="quote-mark">&ldquo;</span>
    <p>Lorem ipsum dolor sit amet, consectetur adipiscing elit. Curabitur lacinia pretium risus ac euismod. A ictor convallis mattis."</p>
    <cite>- John Doe</cite>
  </blockquote>
  <blockquote class="abs quote olive" style="left:345px;top:882px">
    <div class="avatar light" role="img" aria-label="Portrait photo of member Jane Johnson"></div>
    <span class="quote-mark">&ldquo;</span>
    <p>Lorem ipsum dolor sit amet, consectetur adipiscing elit. Curabitur lacinia pretium risus ac euismod."</p>
    <cite>- Jane Johnson</cite>
  </blockquote>
</section>

<footer class="abs footer">
  <div class="abs footer-brand"><span class="brand-mark"></span>Unified Household Wellspring Alliance</div>
  <div class="abs footer-text">
    <p>Lorem ipsum dolor sit amet, consectetur adipiscing elit. Curabitur lacinia pretium risus ac euismod. A ictor convallis mattis. Maecenas ornare augue vel nibh molestie, nec ultrices velit tincidunt.</p>
    <p style="margin-top:10px">Aliquam convallis mattis.Aliquam auctor Maecenas ornare augue vel nibh molestie, nec ultrices velit tincidunt.</p>
  </div>
  <div class="abs" style="left:389px;top:33px">
    <h4>QUICKLINKS</h4>
    <ul>
      <li><span class="dot"></span>Home</li>
      <li><span class="dot"></span>About us</li>
      <li><span class="dot"></span>Member's Benefits</li>
      <li><span class="dot"></span>Our Services</li>
      <li><span class="dot"></span>Contact us</li>
    </ul>
  </div>
  <div class="abs" style="left:516px;top:33px">
    <h4>SOCIAL MEDIA</h4>
    <ul>
      <li><span class="ring"></span>Friendbook</li>
      <li><span class="ring"></span>Chirper</li>
      <li><span class="ring"></span>Snapgram</li>
      <li><span class="ring"></span>Searchplus</li>
    </ul>
  </div>
</footer>
<div class="abs copyright">Copyright &copy; 2017 Unified Household Wellspring Alliance.</div>

</body>
</html>
```